Coastline Haven Retreats Business Card Design

Design a business card for Coastline Haven Retreats. Look at the website for colors and reference. Card should have logo, name, title, office number, mobile number, email, URL and a tagline like, "Luxury Hotel & Resort Email Marketing" (This might change).

https://www.coastlinehavenretreats.example

The rest I will leave up to your imagination.

Contact Information for Business Card

Logo, name, title, office number, mobile number, email, URL and a tagline like, "Luxury Hotel & Resort Email Marketing" (This might change).

```html
<!DOCTYPE html>
<html lang="en">
<head>
<meta charset="utf-8">
<title>Coastline Haven Retreats — Business Card</title>
<link href="https://fonts.googleapis.com/css2?family=Arimo:wght@400;700&display=swap" rel="stylesheet">
<style>
  :root {
    --page: #2b2b2b;
    --card: #1c1c1c;
    --ink: #f2f2f2;
    --ink-soft: #d9d9d9;
    --emboss: #2a2a2a;
    --accent: #f07a12;
  }
  * { box-sizing: border-box; margin: 0; padding: 0; }
  html, body { width: 1200px; height: 915px; overflow: hidden; }
  body {
    background: var(--page);
    font-family: "Arimo", Arial, sans-serif;
    display: flex;
    flex-direction: column;
    align-items: center;
    justify-content: center;
    gap: 40px;
  }
  .card {
    position: relative;
    width: 700px;
    height: 400px;
    background: var(--card);
    border-radius: 22px;
    overflow: hidden;
  }

  /* back side */
  .card--back {
    display: flex;
    flex-direction: column;
    align-items: center;
    justify-content: center;
  }
  .back-wordmark {
    color: var(--emboss);
    font-weight: 700;
    font-size: 44px;
    letter-spacing: 1px;
    text-transform: uppercase;
  }
  .tagline {
    margin-top: 70px;
    color: var(--accent);
    font-size: 20px;
    letter-spacing: 0.3px;
  }

  /* front side */
  .brand {
    position: absolute;
    left: 48px;
    top: 150px;
    display: flex;
    align-items: center;
    gap: 12px;
  }
  .brand-square {
    width: 18px;
    height: 18px;
    background: var(--accent);
  }
  .brand-name {
    color: var(--ink);
    font-weight: 700;
    font-size: 26px;
    text-transform: uppercase;
    letter-spacing: 0.5px;
  }
  .person {
    position: absolute;
    right: 40px;
    top: 56px;
    text-align: right;
  }
  .person-name {
    color: var(--accent);
    font-weight: 700;
    font-size: 30px;
    text-transform: uppercase;
    letter-spacing: 0.5px;
  }
  .person-title {
    color: var(--ink-soft);
    font-size: 17px;
    margin-top: 4px;
  }
  .accent-tab {
    position: absolute;
    right: 0;
    top: 56px;
    width: 22px;
    height: 40px;
    background: var(--accent);
  }
  .address {
    position: absolute;
    left: 48px;
    top: 228px;
    color: var(--ink);
    font-size: 17px;
    line-height: 1.3;
    font-style: normal;
  }
  .contacts {
    position: absolute;
    left: 48px;
    top: 290px;
    list-style: none;
    color: var(--ink);
    font-size: 17px;
  }
  .contacts li {
    display: flex;
    align-items: center;
    gap: 10px;
    line-height: 23px;
  }
  .contacts svg { width: 13px; height: 13px; fill: var(--accent); flex: none; }
</style>
</head>
<body>
  <section class="card card--back" aria-label="Card back">
    <p class="back-wordmark">Coastline Haven Retreats</p>
    <p class="tagline">Luxury Hotel &amp; Resort Email Marketing</p>
  </section>

  <section class="card card--front" aria-label="Card front">
    <div class="person">
      <p class="person-name">Daniel Morrow</p>
      <p class="person-title">CEO/Founder</p>
    </div>
    <span class="accent-tab"></span>

    <div class="brand">
      <span class="brand-square"></span>
      <span class="brand-name">Coastline Haven Retreats</span>
    </div>

    <address class="address">
      Po Box, 48 B Harbor Rd<br>
      North America, AB 20415
    </address>

    <ul class="contacts">
      <li>
        <svg viewBox="0 0 16 16" aria-hidden="true"><path d="M4 0h8a1 1 0 0 1 1 1v14a1 1 0 0 1-1 1H4a1 1 0 0 1-1-1V1a1 1 0 0 1 1-1zm1 2v10h6V2zm3 11a1 1 0 1 0 0 2 1 1 0 0 0 0-2z"/></svg>
        555.214.7300
      </li>
      <li>
        <svg viewBox="0 0 16 16" aria-hidden="true"><path d="M3.6 1l2.5 3-1.5 1.7a9 9 0 0 0 5.7 5.7L12 9.9l3 2.5-1.6 2.6C7 15 1 9 1 2.6z"/></svg>
        +34 600 112 447
      </li>
      <li>
        <svg viewBox="0 0 16 16" aria-hidden="true"><path d="M1 3h14v10H1zm1.5 1.3v.3L8 8.8l5.5-4.2v-.3zM2.5 6.4v5.3h11V6.4L8 10.6z"/></svg>
        info@coastlinehavenretreats.example
      </li>
      <li>
        <svg viewBox="0 0 16 16" aria-hidden="true"><path d="M8 0a8 8 0 1 0 0 16A8 8 0 0 0 8 0zm-1 2.2c-.6 1-1 2.4-1.1 4H2.2A6 6 0 0 1 7 2.2zm2 0a6 6 0 0 1 4.8 4H10.1c-.1-1.6-.5-3-1.1-4zM2.2 8h3.7c.1 1.6.5 3 1.1 4A6 6 0 0 1 2.2 8zm5.7 0h.2c-.1 1.3-.4 2.4-.1 3.3-.4-.9-.6-2-.1-3.3zm2.2 0h3.7A6 6 0 0 1 9 13.8c.6-1 1-2.4 1.1-4.1z"/></svg>
        www.coastlinehavenretreats.example
      </li>
    </ul>
  </section>
</body>
</html>
```